website re-design

require to re design my existing website ( www.norvelcastline.com ) to show a corporate image of the company . i also require an advise on the content editorial text . i am currently using hostaroo for domain registration and website design and publishing .

Target Market(s)

focus on the meddle east market , but visible for worldwide business opportunity

Industry/Entity Type

It Company

Coding

Coded - Design and coding required

Number of Pages Required

5+ page

Requirements
Must have
• --show the brand color when possible ,
• --professional website reflecting the following main key areas :broadcast /media/consultancy services/technology
• --number of pages to be maintained or increased if necessary
• --adaptive design for all PC and mobiles
• --simple to navigate and get the idea quickly
• --landing page with full image and slight movement in the background
Nice to have
• any interactivity with visitors
• font style to be recommended by the designer ( professional test , easy to read )
• more descriptive image and less text
• visitor to know what we do more from graphics , image and video
• landing page to have some motions ( similar to www.quarrytelm.com/ )

```html
<!DOCTYPE html>
<html lang="en">
<head>
<meta charset="utf-8">
<title>Norvel Castline — Technology Innovation</title>
<link rel="stylesheet" href="https://fonts.googleapis.com/css2?family=Open+Sans:wght@400;600;700&family=Raleway:wght@400;500;600&display=swap">
<style>
:root{
  --orange:#f26b0f;
  --orange-dark:#d95c05;
  --black:#0b0b0b;
  --ink:#222;
  --text:#444;
  --muted:#666;
  --dark-band:#1f1f1f;
  --footer:#1c1c1c;
  --white:#fff;
  --line:#d9d9d9;
}
*{box-sizing:border-box;margin:0;padding:0}
html,body{width:1200px;height:3141px;overflow:hidden}
body{position:relative;background:var(--white);font-family:"Open Sans",Arial,sans-serif;color:var(--text)}
.abs{position:absolute}

/* top bar */
.topbar{left:0;top:0;width:1200px;height:32px;background:var(--black)}
.call{position:absolute;left:62px;top:0;height:32px;display:flex;align-items:center;gap:12px;color:var(--white);font-size:13px;font-weight:600}
.call .ico{width:30px;height:32px;background:var(--orange);display:flex;align-items:center;justify-content:center}
.social{position:absolute;right:62px;top:5px;display:flex;gap:8px}
.social span{width:22px;height:22px;border:1.5px solid #ddd;border-radius:50%}

/* header */
.logo{left:59px;top:32px;width:190px;height:150px;background:var(--orange);padding:34px 0 0 16px;color:var(--white);font-family:"Raleway",Arial,sans-serif;font-weight:500;font-size:33px;line-height:31px;letter-spacing:-.5px}
.tagline{left:59px;top:188px;font-size:13px;font-weight:700;color:var(--ink);letter-spacing:.2px}
.contact-item{display:flex;align-items:center;gap:22px;font-size:11.5px;line-height:22px;color:var(--ink)}
.contact-item.address{left:656px;top:72px}
.contact-item.phone{left:906px;top:72px}
.divider{left:885px;top:78px;width:1px;height:36px;background:var(--line)}
.nav{left:402px;top:142px;width:737px;height:44px;background:var(--orange);display:flex;align-items:center;justify-content:space-around;padding:0 18px;font-family:"Raleway",Arial,sans-serif;font-size:16px;color:var(--white)}

/* hero */
.hero{left:0;top:220px;width:1200px;height:488px;background:radial-gradient(ellipse at 50% 45%,#4f8fe0 0%,#1d4f9c 25%,#0d2452 55%,#060c1e 100%)}
.hero-title{left:0;top:470px;width:1200px;text-align:center;color:var(--white);font-size:50px;font-weight:400}
.hero-sub{left:0;top:548px;width:1200px;text-align:center;color:var(--white);font-size:13.5px}
.btn-outline{left:526px;top:588px;width:146px;height:44px;border:2px solid var(--white);color:var(--white);font-size:14px;display:flex;align-items:center;justify-content:center}

/* about */
.section-title{left:0;width:1200px;text-align:center;color:var(--orange);font-family:"Raleway",Arial,sans-serif;font-weight:400;font-size:41px;letter-spacing:.5px}
.about-text{left:147px;top:842px;width:906px;text-align:center;font-size:12.6px;line-height:26px;color:var(--text)}
.service-img{top:1043px;width:277px;height:130px}
.service-cap{top:1190px;width:277px;text-align:center;font-size:19px;line-height:27px;color:var(--ink)}
.btn{background:var(--orange);color:var(--white);display:flex;align-items:center;justify-content:center;font-size:14px}

/* testimonial */
.testimonials{left:0;top:1397px;width:1200px;height:534px;background:var(--dark-band)}
.avatar{left:555px;top:1518px;width:88px;height:88px;border-radius:50%;border:3px solid var(--white);background:radial-gradient(circle at 50% 40%,#c9b6a4 0%,#8a7563 55%,#3b3a3e 100%)}
.quote-card{left:304px;top:1638px;width:592px;height:217px;background:var(--white);text-align:center;padding-top:22px}
.quote-card::before{content:"";position:absolute;left:284px;top:-12px;border:12px solid transparent;border-top:0;border-bottom-color:var(--white)}
.quote-name{color:var(--orange);font-size:21px;font-family:"Raleway",Arial,sans-serif;letter-spacing:.5px}
.quote-role{margin-top:20px;font-size:15.5px;color:var(--ink)}
.quote-text{margin:22px auto 0;width:520px;font-size:12.6px;line-height:27px;color:var(--text)}

/* news */
.title-rule{left:448px;top:2042px;width:304px;height:2px;background:var(--orange)}
.news-img{top:2088px;width:346px;height:205px}
.news-title{top:2319px;width:340px;font-size:13px;font-weight:700;line-height:26px;color:var(--ink)}
.news-date{width:340px;font-size:12.5px;color:var(--ink)}
.news-text{width:340px;font-size:12.5px;line-height:26px;color:var(--text)}

/* partners */
.partner{top:2622px;width:239px;height:109px;border:1.5px solid var(--line);display:flex;align-items:center;justify-content:center;gap:10px;font-size:26px;font-weight:600;color:#1f3554}
.partner .mark{width:12px;height:12px;background:var(--orange);border-radius:50%}

/* footer */
.footer{left:0;top:2760px;width:1200px;height:381px;background:linear-gradient(90deg,#262626 0%,#1b1b1b 60%,#151515 100%)}
.footer-h{top:2815px;font-family:"Raleway",Arial,sans-serif;font-size:21px;color:var(--white)}
.footer-txt{color:#e6e6e6;font-size:12px;line-height:24px}
.menu{top:2862px;display:grid;grid-template-columns:140px 140px;row-gap:11px;font-size:12.5px;color:#eee}
.menu span{display:flex;align-items:center;gap:9px}
.subscribe{left:792px;top:2862px;width:285px;height:40px;background:var(--white)}
.subscribe-btn{left:1077px;top:2862px;width:62px;height:40px;background:var(--orange);display:flex;align-items:center;justify-content:center}
.sub-note{left:792px;top:2940px;font-size:12.5px;color:var(--orange)}
.follow{left:792px;top:2990px;display:grid;grid-template-columns:130px 130px;row-gap:14px;font-size:12px;color:#ddd}
.follow span{display:flex;align-items:center;gap:10px}
.follow i{width:8px;height:8px;border-radius:50%;background:#ccc;display:inline-block}
.copyright{left:61px;top:3091px;width:1078px;height:50px;background:var(--orange);color:var(--white);font-size:12px;display:flex;align-items:center;justify-content:center}
</style>
</head>
<body>

<!-- top bar -->
<div class="abs topbar">
  <div class="call"><span class="ico"><svg width="14" height="14" viewBox="0 0 24 24"><path fill="#fff" d="M6.6 10.8a15 15 0 0 0 6.6 6.6l2.2-2.2c.3-.3.7-.4 1-.2 1.1.4 2.3.6 3.6.6.6 0 1 .4 1 1V20c0 .6-.4 1-1 1A17 17 0 0 1 3 4c0-.6.4-1 1-1h3.5c.6 0 1 .4 1 1 0 1.3.2 2.5.6 3.6.1.3 0 .7-.2 1z"/></svg></span>Call Us Today!</div>
  <div class="social" aria-label="Social links"><span></span><span></span><span></span><span></span><span></span></div>
</div>

<!-- header -->
<div class="abs logo">NORVEL<br>CASTLINE</div>
<div class="abs tagline">TECHNOLOGY INNOVATION</div>
<div class="abs contact-item address">
  <svg width="20" height="28" viewBox="0 0 20 28"><path d="M10 1.5a8 8 0 0 0-8 8c0 6 8 16 8 16s8-10 8-16a8 8 0 0 0-8-8z" fill="none" stroke="#333" stroke-width="1.6"/><circle cx="10" cy="9.5" r="3" fill="none" stroke="#333" stroke-width="1.6"/></svg>
  <div>Norvel Castline FZ-LLC<br>Harbor Media Quarter</div>
</div>
<div class="abs divider"></div>
<div class="abs contact-item phone">
  <svg width="24" height="24" viewBox="0 0 24 24"><path d="M6.6 10.8a15 15 0 0 0 6.6 6.6l2.2-2.2c.3-.3.7-.4 1-.2 1.1.4 2.3.6 3.6.6.6 0 1 .4 1 1V20c0 .6-.4 1-1 1A17 17 0 0 1 3 4c0-.6.4-1 1-1h3.5c.6 0 1 .4 1 1 0 1.3.2 2.5.6 3.6.1.3 0 .7-.2 1z" fill="none" stroke="#333" stroke-width="1.4"/></svg>
  <div>971505550147<br>info@norvelcastline.com</div>
</div>
<nav class="abs nav"><span>Home</span><span>About</span><span>Services</span><span>Solutions</span><span>Customer</span><span>Employment</span><span>Contact</span></nav>

<!-- hero -->
<div class="abs hero" role="img" aria-label="Data centre corridor lined with illuminated server racks in blue light"></div>
<h1 class="abs hero-title">Norvel Castline</h1>
<p class="abs hero-sub">Norvel Castline Provides Broadcast System Solutions and Services to support broadcasters</p>
<div class="abs btn-outline">Read More</div>

<!-- about -->
<h2 class="abs section-title" style="top:778px">NORVEL CASTLINE</h2>
<p class="abs about-text">Norvel Castline is a Technology solution and service provider in the broadcast and telecom media industry . Our objective is to support broadcasters, production house and telecom operators in their migration plan and developing&nbsp; new concepts and ideas that provide an adding value to the internal operation , technology infrastructure and&nbsp; viewer experience . Our team represent a number of expert and professional possessing well over 20 years of experience in Studio and facility design , engineering , integration and support of broadcast , broadband and telecommunication systems . our strong relationship with the regional key player, international manufacture and software developers give us the opportunity to offer the appropriate services and provide the local commitment and support .</p>

<div class="abs service-img" style="left:115px;background:linear-gradient(135deg,#e9f0f6 0%,#b9cbdc 45%,#3d4b60 100%)" role="img" aria-label="Business consultants meeting in a bright office"></div>
<div class="abs service-img" style="left:461px;background:linear-gradient(160deg,#8c7e70 0%,#4b4a52 50%,#22252c 100%)" role="img" aria-label="Engineers working at computer stations in an operations room"></div>
<div class="abs service-img" style="left:808px;background:linear-gradient(135deg,#1a1f2c 0%,#6b2a1e 45%,#d0512a 70%,#26304a 100%)" role="img" aria-label="Close view of network cables with glowing connectors"></div>
<div class="abs service-cap" style="left:115px">Consultancy and<br>Project Management</div>
<div class="abs service-cap" style="left:461px">Engineering and<br>Managed Services</div>
<div class="abs service-cap" style="left:808px">Innovative Broadcast<br>Technology solutions</div>
<div class="abs btn" style="left:530px;top:1273px;width:140px;height:40px">Read More</div>

<!-- testimonials -->
<div class="abs testimonials"></div>
<h2 class="abs section-title" style="top:1450px">SOME WORDS FROM OUR CUSTOMERS</h2>
<div class="abs avatar" role="img" aria-label="Customer portrait"></div>
<div class="abs quote-card">
  <div class="quote-name">DARREN HOLT</div>
  <div class="quote-role">happy customer</div>
  <p class="quote-text">"HomeNest is really excellent site for furnitures. I am very happy with the HomeNest products and dedicated services from them. HomeNest is really excellent site for furnitures"</p>
</div>

<!-- news -->
<h2 class="abs section-title" style="top:1970px">UPDATED NEWS</h2>
<div class="abs title-rule"></div>

<div class="abs news-img" style="left:61px;background:linear-gradient(135deg,#f2f2f2 0%,#cfd6dd 50%,#7b8794 100%)" role="img" aria-label="Hands reviewing printed charts on a desk"></div>
<div class="abs news-img" style="left:427px;background:linear-gradient(160deg,#5a6470 0%,#3f78b0 45%,#233a55 100%)" role="img" aria-label="Blue network cables plugged into a switch"></div>
<div class="abs news-img" style="left:792px;background:linear-gradient(135deg,#d8cfc4 0%,#8b7b6c 50%,#3a3a3e 100%)" role="img" aria-label="Students assembling electronics at a workbench"></div>

<div class="abs news-title" style="left:61px">Storage Trends—Exploring Objects and<br>Scale-Out NAS</div>
<div class="abs news-date" style="left:61px;top:2374px">11/4/2016, 10:30:00 PM</div>
<div class="abs news-text" style="left:61px;top:2398px">Network attached storage, or NAS, continues to<br>expand in acceptance and in capabilities.</div>

<div class="abs news-title" style="left:427px">Q&amp;A: Halvard Drone Chief Evan Marsh</div>
<div class="abs news-date" style="left:427px;top:2348px">11/4/2016, 6:48:00 AM</div>
<div class="abs news-text" style="left:427px;top:2372px">Halvard was flight ready when rules for<br>commercial use of unmanned aerial systems went<br>into effect in late August.</div>

<div class="abs news-title" style="left:792px">Bird Conservancy Hails Tower Changes</div>
<div class="abs news-date" style="left:792px;top:2348px">11/3/2016, 11:31:00 PM</div>
<div class="abs news-text" style="left:792px;top:2372px">A bird conservation group estimates that<br>approximately 750 tall towers in the United States<br>have converted to flashing lights ...</div>

<div class="abs btn" style="left:61px;top:2484px;width:111px;height:38px">Read More</div>
<div class="abs btn" style="left:427px;top:2484px;width:111px;height:38px">Read More</div>
<div class="abs btn" style="left:792px;top:2484px;width:111px;height:38px">Read More</div>

<!-- partners -->
<div class="abs partner" style="left:61px">Veltrion</div>
<div class="abs partner" style="left:339px;font-size:22px">Keystone Advisors</div>
<div class="abs partner" style="left:620px">Orwen</div>
<div class="abs partner" style="left:900px;font-size:23px"><span class="mark"></span>Fivepoint Hub</div>

<!-- footer -->
<div class="abs footer"></div>
<div class="abs footer-h" style="left:61px">Contact Us</div>
<p class="abs footer-txt" style="left:61px;top:2858px;width:250px;line-height:22px">Lorem Ipsum is simply dummy text of the printing and typesetting industry. Lorem Ipsum has been the industry's standard dummy text.</p>
<div class="abs footer-txt" style="left:61px;top:2956px;display:flex;gap:12px;align-items:center">
  <svg width="16" height="12" viewBox="0 0 16 12"><rect x=".8" y=".8" width="14.4" height="10.4" fill="none" stroke="#f26b0f" stroke-width="1.4"/><path d="M1 1l7 5 7-5" fill="none" stroke="#f26b0f" stroke-width="1.4"/></svg>info@norvelcastline.com</div>
<div class="abs footer-txt" style="left:61px;top:2989px;display:flex;gap:12px;align-items:center">
  <svg width="14" height="14" viewBox="0 0 24 24"><path fill="#f26b0f" d="M6.6 10.8a15 15 0 0 0 6.6 6.6l2.2-2.2c.3-.3.7-.4 1-.2 1.1.4 2.3.6 3.6.6.6 0 1 .4 1 1V20c0 .6-.4 1-1 1A17 17 0 0 1 3 4c0-.6.4-1 1-1h3.5c.6 0 1 .4 1 1 0 1.3.2 2.5.6 3.6.1.3 0 .7-.2 1z"/></svg>+971 4 4550182</div>
<div class="abs footer-txt" style="left:61px;top:3018px;display:flex;gap:12px;align-items:flex-start;line-height:20px">
  <svg width="12" height="16" viewBox="0 0 20 28" style="margin-top:3px"><path fill="#f26b0f" d="M10 1a9 9 0 0 0-9 9c0 7 9 17 9 17s9-10 9-17a9 9 0 0 0-9-9zm0 12a3 3 0 1 1 0-6 3 3 0 0 1 0 6z"/></svg>
  <span>Norvel Castline FZ-LLC<br>Harbor Media Quarter</span></div>

<div class="abs footer-h" style="left:398px">Main Menu</div>
<div class="abs menu" style="left:400px">
  <span><svg width="12" height="10" viewBox="0 0 12 10"><path d="M1 5l3.5 3.5L11 1" fill="none" stroke="#f26b0f" stroke-width="2.2"/></svg>Home</span>
  <span><svg width="12" height="10" viewBox="0 0 12 10"><path d="M1 5l3.5 3.5L11 1" fill="none" stroke="#f26b0f" stroke-width="2.2"/></svg>Cutomer</span>
  <span><svg width="12" height="10" viewBox="0 0 12 10"><path d="M1 5l3.5 3.5L11 1" fill="none" stroke="#f26b0f" stroke-width="2.2"/></svg>About Us</span>
  <span><svg width="12" height="10" viewBox="0 0 12 10"><path d="M1 5l3.5 3.5L11 1" fill="none" stroke="#f26b0f" stroke-width="2.2"/></svg>Employment</span>
  <span><svg width="12" height="10" viewBox="0 0 12 10"><path d="M1 5l3.5 3.5L11 1" fill="none" stroke="#f26b0f" stroke-width="2.2"/></svg>Services</span>
  <span><svg width="12" height="10" viewBox="0 0 12 10"><path d="M1 5l3.5 3.5L11 1" fill="none" stroke="#f26b0f" stroke-width="2.2"/></svg>Clients Say</span>
  <span><svg width="12" height="10" viewBox="0 0 12 10"><path d="M1 5l3.5 3.5L11 1" fill="none" stroke="#f26b0f" stroke-width="2.2"/></svg>Solutions</span>
  <span><svg width="12" height="10" viewBox="0 0 12 10"><path d="M1 5l3.5 3.5L11 1" fill="none" stroke="#f26b0f" stroke-width="2.2"/></svg>Our Team</span>
  <span><svg width="12" height="10" viewBox="0 0 12 10"><path d="M1 5l3.5 3.5L11 1" fill="none" stroke="#f26b0f" stroke-width="2.2"/></svg>Blog</span>
  <span><svg width="12" height="10" viewBox="0 0 12 10"><path d="M1 5l3.5 3.5L11 1" fill="none" stroke="#f26b0f" stroke-width="2.2"/></svg>Contact</span>
</div>

<div class="abs footer-h" style="left:792px">Subscribe to Our News Feed</div>
<div class="abs subscribe"></div>
<div class="abs subscribe-btn"><svg width="20" height="14" viewBox="0 0 20 14"><rect x="1" y="1" width="18" height="12" fill="none" stroke="#fff" stroke-width="1.6"/><path d="M1 1l9 6 9-6" fill="none" stroke="#fff" stroke-width="1.6"/></svg></div>
<div class="abs sub-note">Get Latest updates and offers.</div>
<div class="abs follow">
  <span><i></i>Friendlane</span><span><i></i>Circlecast</span>
  <span><i></i>Chirpline</span><span><i></i>Proflink</span>
</div>

<div class="abs copyright">© 2016 norvel castline. Right Reserved.</div>

</body>
</html>
```